Rollvane Supply .com

This website is simple!!!
Landing page background image should capture the customers attention!!! We will provide a image as a example of what we like. The purpose for this website is to provide customers with a clean easy way to request a quote for industrial casters and wheels by OEM’s as well as maintenance departments worldwide. Please see if you can follow our thought process below.
Customer comes to website, they are invited to Request a Quote by providing us with Manufacturer Name, Manufacturers Part # and quantity needed.
If this is not known the customer will complete will WP conversation format form answering about 10 questions
Or
Look up the part number in one of the 8 to 12 catalogs located in the Pagewhirl Deck format on our catalog page, or equal plug in .
When the client request a quote a account page will pop up request The following:
Clients first and last name
Email address
And optional questions
Company name and best contact number.
Once this is complete customer will hit SUBMIT.
The customers request will be in system. A email will be sent to Customer service notifying us the Quote Request has been made.
We will then build a quote for the customer with a good, better and best options. Customers Request a Quote submission may have more than one caster or wheel requested at a time, so website must allow this.
When the customer comes back into website there email address will come up as the account name and request a password be made for them. This will allow them to store quotes in their account for future needs. If quote is older than 30 day the system will trigger a button at the bottom of the quote for resubmit Request for updated quote.
Once customer reviews quote the quote can be Converted to order within the website.
Once Converted the system will send us a email and order will be processed.
We will need a Chat program that will text to CS the questions.
You will need to have high quality graphic design skills on your team.
We have found 2 plugins that would work nicely with our new website Pagewhirl decks to showcase our catalogs for customers to research and QuillKit conversation forms to complete request for quote form.
Just Ideas:
Very very ghosted caster blueprint in white background but very very ghosted or the icon just idea
We have never had a font used we like
Grayscale every except for rubber on wheels and logo icon
Website should have hamburger menu on left
Website should hav responsive deign
Account head on right side
Has anyone read the brief from top to bottom and the updates, I’m seeing a lot of duplicates of the website I posted in images I want a clean website With lite backgrand with the poly being definite colors on each wheel I added a green yellow and red image has anyone looked at that Just a question?
Went on vacation/holiday

```html
<!DOCTYPE html>
<html lang="en">
<head>
<meta charset="utf-8">
<title>Rollvane Supply .com</title>
<link href="https://fonts.googleapis.com/css2?family=Poppins:wght@400;500;600;700;800&display=swap" rel="stylesheet">
<style>
:root{
  --navy:#2b4499;
  --sky:#4fa3f2;
  --ink:#222;
  --muted:#8a8a8a;
  --field:#f1f1f3;
  --paper:#ffffff;
  --mist:#f4f4f5;
  --grid:#eceef2;
}
*{margin:0;padding:0;box-sizing:border-box}
html,body{width:1200px;height:2967px;overflow:hidden}
body{position:relative;font-family:'Poppins',sans-serif;color:var(--ink);
  background-color:var(--paper);
  background-image:linear-gradient(var(--grid) 1px,transparent 1px),linear-gradient(90deg,var(--grid) 1px,transparent 1px);
  background-size:24px 24px;background-repeat:repeat;background-position:0 0}
.page-lower{position:absolute;left:0;top:1200px;width:1200px;height:1767px;background:var(--paper)}

/* header */
.brand{position:absolute;left:89px;top:30px;display:flex;align-items:center;gap:10px;color:var(--navy);font-weight:700;font-size:17px}
.brand-dot{width:26px;height:26px;border-radius:50%;background:var(--navy)}
.header-tools{position:absolute;left:1042px;top:24px;display:flex;gap:16px;align-items:center}

/* hero */
.hero-title{position:absolute;left:115px;top:282px;z-index:2;color:var(--navy);font-weight:800;line-height:1;letter-spacing:1px}
.hero-title .big{display:block;font-size:104px}
.hero-title .small{display:block;font-size:66px;margin:8px 0 0 156px}
.hero-photo{position:absolute;left:620px;top:92px;width:520px;height:565px;border-radius:46% 40% 48% 44%;
  background:radial-gradient(circle at 45% 65%,#2f5fd0 0,#3c55b8 35%,#b9c3cf 60%,rgba(255,255,255,0) 72%)}
.wave{position:absolute;left:0;top:600px}
.solutions{position:absolute;left:0;top:750px;width:1200px;text-align:center;color:#fff;font-weight:700;font-size:38px;line-height:1.05}
.steps{position:absolute;left:337px;top:853px;display:flex;gap:11px}
.step{width:168px;height:167px;border-radius:14px;background:#fff;color:#333;text-align:center;font-size:16px;line-height:1.25;padding-top:26px}
.step.active{background:var(--sky);color:#fff}
.step-icon{position:relative;width:60px;height:64px;margin:0 auto 12px}
.step-badge{position:absolute;right:-4px;top:-6px;width:21px;height:21px;border-radius:50%;background:var(--sky);color:#fff;font-size:11px;line-height:21px;text-align:center}
.step.active .step-badge{background:#fff;color:var(--sky)}
.hero-actions{position:absolute;left:438px;top:1047px;display:flex;gap:7px}
.pill{height:41px;border-radius:21px;font-weight:700;font-size:13px;display:flex;align-items:center;justify-content:center;letter-spacing:.3px}
.pill.fill{width:159px;background:var(--sky);color:#fff}
.pill.line{width:158px;border:2px solid #fff;color:#fff}

/* about */
.about{position:absolute;left:152px;top:1434px;width:430px}
.about h2{color:var(--navy);font-weight:700;font-size:45px;line-height:.92}
.about p{margin-top:16px;width:390px;font-size:14.3px;line-height:22.4px;color:#333}
.read-more{margin-top:16px;width:129px;height:41px;border:2px solid var(--sky);border-radius:21px;display:flex;align-items:center;justify-content:center;font-weight:700;font-size:13px;color:#222;margin-left:-5px}

.quote-card{position:absolute;left:614px;top:1319px;width:415px;height:467px;background:#fff;border-radius:14px;box-shadow:0 10px 40px rgba(0,0,0,.08);padding:44px 38px 0}
.quote-card h3{text-align:center;color:var(--navy);font-weight:700;font-size:34px;margin-bottom:20px}
.field-label{color:var(--navy);font-weight:600;font-size:16px;margin-bottom:6px}
.field{height:45px;background:var(--field);border-radius:7px;padding-left:21px;display:flex;align-items:center;font-size:14px;color:#666;margin-bottom:14px}
.field.select{justify-content:space-between;padding-right:16px;color:#333;font-weight:600}
.submit{height:43px;border-radius:22px;background:var(--sky);color:#fff;font-weight:700;font-size:16px;display:flex;align-items:center;justify-content:center;letter-spacing:.5px;margin-top:2px;width:340px}

/* resubmit */
.resubmit-title{position:absolute;left:0;top:1886px;width:1200px;text-align:center;color:var(--navy);font-weight:700;font-size:46px;line-height:1.08}
.products{position:absolute;left:90px;top:2033px;display:flex;gap:14px}
.product{position:relative;width:245px;height:300px}
.product-bg{position:absolute;left:0;top:23px;width:245px;height:277px;background:#fff;border-radius:10px;box-shadow:0 8px 30px rgba(0,0,0,.07)}
.product-photo{position:absolute;left:40px;top:0;width:165px;height:179px;border-radius:40%}
.product-info{position:absolute;left:0;top:197px;width:245px;text-align:center}
.product-info h4{font-weight:600;font-size:21px;color:#222}
.price{font-weight:600;font-size:20px;color:#8a8a8a;line-height:1.3}
.resubmit-link{font-weight:600;font-size:14px;color:var(--sky)}

/* cta */
.footer-bg{position:absolute;left:0;top:2520px}
.cta{position:absolute;left:89px;top:2434px;width:1021px;height:138px;border-radius:69px;background:var(--sky)}
.cta p{position:absolute;left:63px;top:44px;color:#fff;font-weight:700;font-size:41px;line-height:1.2}
.cta .btn{position:absolute;left:755px;top:40px;width:218px;height:57px;border-radius:29px;background:#fff;color:#222;font-weight:700;font-size:16px;display:flex;align-items:center;justify-content:center}

/* footer */
.footer-brand{position:absolute;left:0;top:2745px;width:1200px;display:flex;justify-content:center;align-items:center;gap:12px;color:var(--navy);font-weight:700;font-size:24px}
.footer-brand .brand-dot{width:34px;height:34px}
.footer-nav{position:absolute;left:0;top:2788px;width:1200px;display:flex;justify-content:center;gap:26px;font-size:15px;color:#333}
.socials{position:absolute;left:528px;top:2828px;display:flex;gap:8px}
.social{width:30px;height:30px;border-radius:50%;background:#fff;box-shadow:0 2px 6px rgba(0,0,0,.12);display:flex;align-items:center;justify-content:center}
.social span{width:8px;height:8px;border-radius:50%;background:var(--navy)}
.rule{position:absolute;left:89px;top:2918px;width:1021px;height:1px;background:#dcdcdc}
.copyright{position:absolute;left:0;top:2933px;width:1200px;text-align:center;font-size:14px;color:#333}
.chat{position:absolute;left:1111px;top:2884px;width:54px;height:54px;border-radius:50%;background:var(--navy);display:flex;align-items:center;justify-content:center}
</style>
</head>
<body>
<div class="page-lower"></div>

<header>
  <div class="brand"><span class="brand-dot"></span>Rollvane Supply .com</div>
  <div class="header-tools">
    <svg width="22" height="24" viewBox="0 0 22 24" fill="none" stroke="#2b4499" stroke-width="1.8"><circle cx="11" cy="7" r="5.5"/><path d="M1.5 23c0-5.5 4.2-9 9.5-9s9.5 3.5 9.5 9"/></svg>
    <svg width="30" height="20" viewBox="0 0 30 20" stroke="#2b4499" stroke-width="2.6" stroke-linecap="round"><path d="M2 3h26M6 10h22M2 17h26"/></svg>
  </div>
</header>

<section class="hero">
  <svg class="wave" width="1200" height="770" viewBox="0 0 1200 770" aria-hidden="true">
    <path d="M0 212 C280 95 560 30 820 28 C960 28 1090 38 1200 50 L1200 758 C1080 660 900 570 600 563 C360 560 170 590 0 621 Z" fill="#2b4499"/>
    <path d="M0 621 C170 590 360 560 600 563 C900 570 1080 660 1200 758 L1200 735 C1080 640 900 552 600 548 C360 546 170 580 0 614 Z" fill="#4fa3f2"/>
  </svg>
  <div class="hero-photo" role="img" aria-label="Swivel caster with blue polyurethane wheel beside a loose blue wheel"></div>
  <h1 class="hero-title"><span class="big">ROLLVANE</span><span class="small">SUPPLY</span></h1>
  <h2 class="solutions">#1 Solutions for all your<br>Applications</h2>
  <div class="steps">
    <div class="step">
      <div class="step-icon"><svg width="60" height="64" viewBox="0 0 60 64" fill="none" stroke="#2b4499" stroke-width="2"><path d="M10 12h26l8 8v36H10z"/><path d="M17 32h20M17 39h14M17 46h10"/><circle cx="44" cy="48" r="10" fill="#fff"/><path d="M39 48l4 4 7-7"/></svg><span class="step-badge">1</span></div>
      Request a<br>Quote
    </div>
    <div class="step active">
      <div class="step-icon"><svg width="60" height="64" viewBox="0 0 60 64" fill="none" stroke="#fff" stroke-width="2"><path d="M12 8h36v50H12z"/><circle cx="30" cy="24" r="9"/><path d="M30 16v16M27 20h5a2 2 0 010 4h-4a2 2 0 000 4h5"/><path d="M18 40h24M18 46h24M18 52h16"/></svg><span class="step-badge">2</span></div>
      Receive a<br>Quote
    </div>
    <div class="step">
      <div class="step-icon"><svg width="60" height="64" viewBox="0 0 60 64" fill="none" stroke="#2b4499" stroke-width="2"><path d="M14 8h30v46H14z"/><path d="M20 16h18M20 22h18"/><path d="M6 34l12-6 12 6v14l-12 6-12-6z"/><path d="M6 34l12 6 12-6M18 40v14"/><circle cx="38" cy="40" r="8" fill="#fff"/><path d="M44 46l7 8"/></svg><span class="step-badge">3</span></div>
      Convert a Quote<br>to order
    </div>
  </div>
  <div class="hero-actions">
    <div class="pill fill">REQUEST QUOTE</div>
    <div class="pill line">CATALOG</div>
  </div>
</section>

<section class="about">
  <h2>About<br>Rollvane Supply</h2>
  <p>Lorem Ipsum is simply dummy text of the printing and typesetting industry. Lorem Ipsum has been the industry's standard dummy text ever since the 1500s, when an unknown printer took a galley of type and scrambled it to make a type specimen book. ..</p>
  <div class="read-more">READ MORE</div>
</section>

<section class="quote-card">
  <h3>Request a Quote</h3>
  <div class="field-label">Manufacturer Name</div>
  <div class="field">Enter Name</div>
  <div class="field-label">Manufacturers Part #</div>
  <div class="field">Enter part #</div>
  <div class="field-label">Quantity needed</div>
  <div class="field select">5<svg width="14" height="9" viewBox="0 0 14 9" fill="none" stroke="#222" stroke-width="2"><path d="M1 1l6 6 6-6"/></svg></div>
  <div class="submit">SUBMIT QUOTE</div>
</section>

<section>
  <h2 class="resubmit-title">Resubmit Request for<br>updated quote</h2>
  <div class="products">
    <div class="product"><div class="product-bg"></div><div class="product-photo" role="img" aria-label="Swivel caster with yellow wheel and brake" style="background:radial-gradient(circle at 50% 60%,#e0a52a 0,#d9b55a 40%,#e6e8ec 62%,rgba(255,255,255,0) 72%)"></div><div class="product-info"><h4>Heading Here</h4><div class="price">$52.00</div><div class="resubmit-link">Resubmit quote</div></div></div>
    <div class="product"><div class="product-bg"></div><div class="product-photo" role="img" aria-label="Swivel caster with red wheel" style="background:radial-gradient(circle at 50% 60%,#c8202d 0,#d0404a 40%,#e6e8ec 62%,rgba(255,255,255,0) 72%)"></div><div class="product-info"><h4>Heading Here</h4><div class="price">$52.00</div><div class="resubmit-link">Resubmit quote</div></div></div>
    <div class="product"><div class="product-bg"></div><div class="product-photo" role="img" aria-label="Swivel caster with black wheel and brake" style="background:radial-gradient(circle at 50% 60%,#1c1c1c 0,#3a3a3a 40%,#e6e8ec 62%,rgba(255,255,255,0) 72%)"></div><div class="product-info"><h4>Heading Here</h4><div class="price">$52.00</div><div class="resubmit-link">Resubmit quote</div></div></div>
    <div class="product"><div class="product-bg"></div><div class="product-photo" role="img" aria-label="Chrome stem caster with black and white wheel" style="background:radial-gradient(circle at 50% 60%,#eaeaea 0,#222 35%,#cfd3d8 58%,rgba(255,255,255,0) 70%)"></div><div class="product-info"><h4>Heading Here</h4><div class="price">$52.00</div><div class="resubmit-link">Resubmit quote</div></div></div>
  </div>
</section>

<svg class="footer-bg" width="1200" height="447" viewBox="0 0 1200 447" aria-hidden="true">
  <path d="M0 176 C300 40 700 -10 1200 10 L1200 447 L0 447 Z" fill="#f4f4f5"/>
</svg>

<section class="cta">
  <p>If quote is older than 30 day</p>
  <div class="btn">RESUBMIT</div>
</section>

<footer>
  <div class="footer-brand"><span class="brand-dot"></span>Rollvane Supply .com</div>
  <nav class="footer-nav"><span>Home</span><span>Resubmit</span><span>Request Quote</span><span>About</span><span>Contact Us</span></nav>
  <div class="socials">
    <div class="social"><span></span></div><div class="social"><span></span></div><div class="social"><span></span></div><div class="social"><span></span></div>
  </div>
  <div class="rule"></div>
  <div class="copyright">©Copyright 2022 | All Rights Reserved</div>
  <div class="chat"><svg width="28" height="24" viewBox="0 0 28 24" fill="#fff"><path d="M14 1C6.8 1 1 5.6 1 11.2c0 3 1.6 5.6 4.2 7.5L4 23l5.2-2.7c1.5.4 3.1.6 4.8.6 7.2 0 13-4.6 13-9.7S21.2 1 14 1z"/><circle cx="8.5" cy="11" r="1.8" fill="#2b4499"/><circle cx="14" cy="11" r="1.8" fill="#2b4499"/><circle cx="19.5" cy="11" r="1.8" fill="#2b4499"/></svg></div>
</footer>
</body>
</html>
```